VELUNDO Brisbane Tiling Service

My name is Mirko Bostel i need a business card for a new company. We are wall and floor tilers based in Brisbane, our company is Velundio Brisbane Tiling Service.
We would like a logo from our website used on our cards. Our website is www.velundio.com.au

I would like my Facebook and Twitter accounts on my card.

Industry/Entity Type

Business

Colors
0692cd
3176b5
33a6d7
85cae6

```html
<!DOCTYPE html>
<html lang="en">
<head>
<meta charset="utf-8">
<title>Velundio Brisbane Tiling Service – Business Card</title>
<link href="https://fonts.googleapis.com/css2?family=Arimo:wght@400&family=Lato:wght@700&display=swap" rel="stylesheet">
<style>
  :root {
    --backdrop: #e9ecef;
    --navy: #27507b;
    --band-light: #3a9ad6;
    --band-deep: #1566a8;
    --brand-blue: #2a7ec0;
    --tile-blue: #1e78bf;
    --paper: #ffffff;
    --tagline: #27507b;
  }
  * { margin: 0; padding: 0; box-sizing: border-box; }
  html, body {
    width: 1200px; height: 1000px; overflow: hidden;
    background: var(--backdrop);
  }
  .canvas { position: relative; width: 1200px; height: 1000px; }

  .card { position: absolute; width: 567px; height: 332px; overflow: hidden; }
  .card-band {
    position: absolute; left: 0; right: 0; bottom: 0; height: 28px;
    background: linear-gradient(90deg, var(--band-light), var(--band-deep));
  }

  /* Front */
  .card-front { left: 120px; top: 123px; background: var(--navy); }
  .front-mark {
    position: absolute; left: 94px; top: 112px;
    display: flex; align-items: center; gap: 14px;
  }
  .front-mark .mark-square { width: 40px; height: 40px; background: var(--paper); }
  .front-mark .mark-name {
    font-family: "Arimo", sans-serif; font-size: 34px; color: var(--paper);
  }
  .service-list {
    position: absolute; left: 315px; top: 86px; list-style: none;
    font-family: "Arimo", sans-serif; font-size: 15px; line-height: 24px;
    color: var(--paper);
  }

  /* Back */
  .card-back { left: 486px; top: 542px; background: var(--paper); }
  .brand-square {
    position: absolute; left: 44px; top: 42px; width: 98px; height: 96px;
    background: var(--tile-blue);
  }
  .brand-name {
    position: absolute; left: 158px; top: 38px;
    font-family: "Arimo", sans-serif; font-size: 50px; line-height: 56px;
    color: var(--brand-blue);
  }
  .brand-tagline {
    position: absolute; left: 163px; top: 96px;
    font-family: "Arimo", sans-serif; font-size: 24px; line-height: 28px;
    color: var(--tagline);
  }
  .contact-panel {
    position: absolute; left: 0; right: 0; top: 177px; height: 126px;
    background: var(--navy);
    font-family: "Lato", sans-serif; font-weight: 700; font-size: 13px;
    line-height: 19.5px; color: var(--paper);
  }
  .contact-details { position: absolute; left: 45px; top: 32px; }
  .registration { position: absolute; left: 409px; top: 71px; }
</style>
</head>
<body>
<div class="canvas">

  <section class="card card-front" aria-label="Card front">
    <div class="front-mark">
      <span class="mark-square"></span>
      <span class="mark-name">velundio</span>
    </div>
    <ul class="service-list">
      <li>Wall &amp; Floor Tiling</li>
      <li>Bathroom Renovations</li>
      <li>Kitchen Splashback Tiling</li>
      <li>Tiling Repairs &amp; Maintenance</li>
      <li>Swimming Pool Tiling</li>
      <li>and much more</li>
    </ul>
    <div class="card-band"></div>
  </section>

  <section class="card card-back" aria-label="Card back">
    <div class="brand-square"></div>
    <div class="brand-name">velundio</div>
    <div class="brand-tagline">brisbane tiling service</div>
    <div class="contact-panel">
      <div class="contact-details">
        <p>Tel: 0412 563 208 / 07 3198 4725</p>
        <p>Email: info@velundio.com.au</p>
        <p>Website: www.velundio.com.au</p>
        <p>27 Harlow Street, Greenslopes, Brisbane, QLD</p>
      </div>
      <div class="registration">
        <p>ABN:48217360954</p>
        <p>QBCC:1093427</p>
      </div>
    </div>
    <div class="card-band"></div>
  </section>

</div>
</body>
</html>
```